Web design project for exciting Australian start-up

Background
We are looking for a creative and talented web design artist to work alongside our market leading web developer.
• You will be required to create a modern and clean design theme for our website, incorporating selected rustic colour scheme elements for our exciting Australian start-up to operate within the coffee industry.
reoccurring work to be expected to flow to the successful designer.
Requirements
• c. 5 - 10 page website
• Landing page
• Log in/ out
• 404 template
• Typography is emphasised
• Please use either a) quillnest.com, b) free web fonts, c) plovra fonts
• All design elements in vector format
• Preferably with icons for each header title(i.e. about us, how it works etc) but designer have free reign over how the site looks, so might not be applicable
• All pages to be responsive
• Down to Kelvo resolution

High level visual design brief attached - additional pages to be worked from base design.

Design inspiration
• We would like to use design elements from the following sources:
http://www.plovra.com/vintel/ (Functionality)
Colour scheme refer to logo and complementary style guide

```html
<!DOCTYPE html>
<html lang="en">
<head>
<meta charset="utf-8">
<title>Brewline – Australia First Online Coffee Market Place</title>
<link href="https://fonts.googleapis.com/css2?family=Roboto+Condensed:ital,wght@0,400;0,700;1,700&family=Open+Sans:wght@300;400&display=swap" rel="stylesheet">
<style>
  :root {
    --orange: #f7872a;
    --orange-line: #f0913f;
    --white: #ffffff;
    --cream: rgba(250, 240, 225, 0.86);
    --footer-bg: #e8e8e8;
    --footer-bar: #bdbdbd;
    --heading: #4a4a4a;
    --text: #555555;
    --muted: #9a9a9a;
    --rule: #c9c9c9;
    --dark: #222222;
  }
  * { box-sizing: border-box; margin: 0; padding: 0; }
  html, body { width: 1200px; height: 756px; overflow: hidden; background: var(--white); }
  body { position: relative; font-family: "Open Sans", sans-serif; }

  .hero-photo {
    position: absolute; left: 0; top: 0; width: 1200px; height: 560px;
    background:
      radial-gradient(ellipse 260px 200px at 840px 320px, #f4f1ec 0%, #e9e3da 55%, rgba(233,227,218,0) 100%),
      radial-gradient(ellipse 380px 260px at 980px 200px, #b4926a 0%, rgba(160,120,80,0) 100%),
      radial-gradient(ellipse 340px 200px at 560px 330px, #5a3218 0%, rgba(90,50,24,0) 100%),
      linear-gradient(180deg, #3a2414 0%, #c0843f 14%, #6b4527 30%, #5b4030 60%, #4a3426 100%);
  }

  .site-header {
    position: absolute; left: 0; top: 0; width: 1200px; height: 67px;
    background: var(--cream);
  }
  .brand {
    position: absolute; left: 103px; top: 18px;
    display: flex; align-items: center; gap: 8px;
    font-family: "Roboto Condensed", sans-serif; font-weight: 700;
    font-size: 22px; letter-spacing: 1px; color: var(--dark);
  }
  .brand-dot { width: 30px; height: 30px; border-radius: 50%; background: var(--orange); }

  .auth { position: absolute; left: 924px; top: 17px; display: flex; height: 32px;
    font-family: "Roboto Condensed", sans-serif; font-weight: 700; font-size: 14px; }
  .auth a { display: flex; align-items: center; justify-content: center; text-decoration: none; }
  .auth .login { width: 89px; background: var(--white); color: var(--orange); border: 1px solid var(--orange); }
  .auth .signup { width: 98px; background: var(--orange); color: var(--dark); }

  .hero-title {
    font-family: "Roboto Condensed", sans-serif; font-weight: 700; color: var(--white);
    text-transform: uppercase; line-height: 1; white-space: nowrap;
  }
  .hero-title span { position: absolute; left: 101px; display: block; }
  .hero-title .big { top: 208px; font-size: 80px; letter-spacing: -1px; }
  .hero-title .sub { font-size: 40px; }
  .hero-title .line-2 { top: 280px; }
  .hero-title .line-3 { top: 320px; }

  .watch-video {
    position: absolute; left: 102px; top: 368px; width: 321px; height: 65px;
    display: flex; text-decoration: none; border: 1px solid var(--white);
  }
  .watch-video .icon { width: 66px; background: var(--white); display: flex; align-items: center; justify-content: center; }
  .watch-video .label {
    flex: 1; background: var(--orange); color: var(--white);
    font-family: "Roboto Condensed", sans-serif; font-weight: 700; font-style: italic;
    font-size: 33px; display: flex; align-items: center; justify-content: center; padding-left: 6px;
  }

  .hero-rule { position: absolute; left: 0; top: 560px; width: 1200px; height: 3px; background: var(--orange-line); }

  .site-footer { position: absolute; left: 0; top: 563px; width: 1200px; height: 179px; background: var(--footer-bg); }
  .footer-col { position: absolute; top: 32px; }
  .footer-col h3 {
    font-family: "Roboto Condensed", sans-serif; font-weight: 700; font-size: 18px;
    color: var(--heading); padding-bottom: 2px; border-bottom: 1px solid var(--rule); display: inline-block;
  }
  .footer-col ul { list-style: none; margin-top: 4px; }
  .footer-col li { position: relative; font-size: 12.5px; line-height: 20.5px; color: var(--text); font-weight: 400; }
  .footer-col li.active::before {
    content: ""; position: absolute; left: -12px; top: 8px; width: 5px; height: 5px; border-radius: 50%; background: var(--orange);
  }
  .col-info { left: 100px; }
  .col-info ul, .col-who ul { padding-left: 9px; }
  .col-who { left: 280px; }
  .col-social { left: 994px; }
  .col-social h3 { width: 88px; }
  .col-social ul { margin-top: 10px; }
  .col-social li { display: flex; align-items: center; gap: 8px; line-height: 25px; }
  .social-mark { width: 17px; height: 17px; border-radius: 3px; display: inline-block; }
  .mark-chirp { background: #4aa9d8; }
  .mark-link { background: #1d87bd; }
  .mark-stream { background: #c9302c; }

  .copyright { position: absolute; left: 93px; top: 161px; font-size: 12px; font-weight: 300; color: var(--muted); }
  .bottom-bar { position: absolute; left: 0; top: 746px; width: 1200px; height: 10px; background: var(--footer-bar); }
</style>
</head>
<body>
  <div class="hero-photo" role="img" aria-label="Photo of a white cup of coffee on a saucer with cinnamon sticks and roasted coffee beans spilling from a burlap sack on a rustic wooden table"></div>

  <header class="site-header">
    <div class="brand"><span class="brand-dot"></span>BREWLINE</div>
    <nav class="auth">
      <a class="login" href="#">Login</a>
      <a class="signup" href="#">Sing Up</a>
    </nav>
  </header>

  <h1 class="hero-title">
    <span class="big">Australia</span>
    <span class="sub line-2">First online cofee</span>
    <span class="sub line-3">market place</span>
  </h1>

  <a class="watch-video" href="#">
    <span class="icon">
      <svg width="44" height="44" viewBox="0 0 44 44" aria-hidden="true">
        <circle cx="22" cy="22" r="21" fill="var(--orange)"/>
        <circle cx="22" cy="22" r="16" fill="none" stroke="var(--white)" stroke-width="2"/>
        <path d="M17 13 L31 22 L17 31 Z" fill="var(--white)"/>
      </svg>
    </span>
    <span class="label">WATCH VIDEO</span>
  </a>

  <div class="hero-rule"></div>

  <footer class="site-footer">
    <section class="footer-col col-info">
      <h3>Helpful Info</h3>
      <ul>
        <li class="active">About us</li>
        <li>Media enquiries</li>
        <li>Terms &amp; conditions</li>
        <li>Privacy policy</li>
      </ul>
    </section>
    <section class="footer-col col-who">
      <h3>Who we are</h3>
      <ul>
        <li class="active">How it works</li>
        <li>FAQ</li>
        <li>Contact us</li>
      </ul>
    </section>
    <section class="footer-col col-social">
      <h3>Join us on</h3>
      <ul>
        <li><span class="social-mark mark-chirp"></span>Chirpline</li>
        <li><span class="social-mark mark-link"></span>Linkora</li>
        <li><span class="social-mark mark-stream"></span>Streamora</li>
      </ul>
    </section>
    <p class="copyright">Copy right 2014 brewline</p>
  </footer>
  <div class="bottom-bar"></div>
</body>
</html>
```